Kelmora Legal Business Card

I require a corporate business card for a new legal services business.

I do not have a logo, nor do I want one.

I require a clean, neat a professional card for a law firm.

Details:

Business Name: Kelmora Legal
Name: Debra Lindqvist
Title: Corporate Services Manager
Location: Office 14 (Top Floor), Toravel Business Centre, Quinlan Grove Street, Alotau CBD, Milne Bay Province.
Postal Address: PO Box 593, Alotau, 211, Milne Bay Province, Papua New Guinea.
Contact: T: +675 6418250, F: +675 6413362, M: +675 72915867, E: dlindqvist@kelmoraexample.com.pg.

I look forward to your design submissions.

Industry/Entity Type

Legal

```html
<!DOCTYPE html>
<html lang="en">
<head>
<meta charset="UTF-8">
<title>Kelmora Legal Business Card</title>
<link href="https://fonts.googleapis.com/css2?family=Lato:wght@400;700&display=swap" rel="stylesheet">
<style>
  :root {
    --backdrop: #2e2e2e;
    --card: #ffffff;
    --brand-blue: #2a6cb5;
    --light-blue: #45a2df;
    --rule-blue: #a9cdee;
    --label-text: #ffffff;
  }
  html, body {
    margin: 0;
    padding: 0;
    width: 1200px;
    height: 900px;
    overflow: hidden;
    background: var(--backdrop);
    font-family: "Lato", sans-serif;
  }
  .card {
    position: absolute;
    left: 75px;
    top: 150px;
    width: 1050px;
    height: 600px;
    background: var(--card);
    box-sizing: border-box;
  }
  .firm-name {
    position: absolute;
    top: 88px;
    left: 0;
    width: 100%;
    margin: 0;
    text-align: center;
    font-size: 52px;
    font-weight: 700;
    letter-spacing: 1px;
    color: var(--brand-blue);
    line-height: 1;
  }
  .office-address {
    position: absolute;
    top: 160px;
    left: 0;
    width: 100%;
    margin: 0;
    text-align: center;
    font-size: 25px;
    line-height: 34px;
    color: var(--light-blue);
    font-style: normal;
  }
  .rule {
    position: absolute;
    left: 0;
    width: 100%;
    height: 2px;
    background: var(--rule-blue);
  }
  .rule--upper { top: 278px; }
  .rule--lower { top: 410px; }
  .person {
    position: absolute;
    left: 50px;
    top: 298px;
  }
  .person-name {
    margin: 0;
    font-size: 38px;
    font-weight: 700;
    color: var(--brand-blue);
    line-height: 46px;
  }
  .person-title {
    margin: 0;
    font-size: 26px;
    color: var(--light-blue);
    line-height: 34px;
  }
  .postal {
    position: absolute;
    left: 520px;
    top: 306px;
    margin: 0;
    font-size: 23px;
    line-height: 33px;
    color: var(--light-blue);
    font-style: normal;
  }
  .postal strong { font-weight: 700; }
  .contact {
    position: absolute;
    display: flex;
    align-items: center;
    height: 42px;
  }
  .contact-label {
    display: inline-block;
    height: 42px;
    line-height: 42px;
    padding: 0 14px;
    background: var(--brand-blue);
    color: var(--label-text);
    font-size: 25px;
    box-sizing: border-box;
  }
  .contact-value {
    margin-left: 20px;
    font-size: 25px;
    color: var(--light-blue);
  }
  .contact--phone  { left: 50px;  top: 460px; }
  .contact--mobile { left: 50px;  top: 528px; }
  .contact--fax    { left: 520px; top: 452px; }
  .contact--email  { left: 520px; top: 520px; }
  .contact--phone .contact-label,
  .contact--mobile .contact-label { width: 132px; }
  .contact--fax .contact-label,
  .contact--email .contact-label { width: 98px; }
  .contact--email .contact-value { font-size: 22px; margin-left: 16px; }
</style>
</head>
<body>
  <section class="card" aria-label="Kelmora Legal business card">
    <h1 class="firm-name">KELMORA LEGAL</h1>
    <address class="office-address">
      Office 14 (Top Floor), Toravel Business Centre,<br>
      Quinlan Grove Street, Alotau CBD, Milne Bay Province.
    </address>

    <div class="rule rule--upper"></div>

    <div class="person">
      <p class="person-name">Debra Lindqvist</p>
      <p class="person-title">Corporate Services Manager</p>
    </div>

    <address class="postal">
      <strong>Postal Address:</strong> PO Box 593, Alotau, 211,<br>
      Milne Bay Province, Papua New Guinea
    </address>

    <div class="rule rule--lower"></div>

    <div class="contact contact--phone">
      <span class="contact-label">phone</span>
      <span class="contact-value">+ 675 6418250</span>
    </div>
    <div class="contact contact--mobile">
      <span class="contact-label">mobile</span>
      <span class="contact-value">+ 675 72915867</span>
    </div>
    <div class="contact contact--fax">
      <span class="contact-label">fax</span>
      <span class="contact-value">+ 675 6413362</span>
    </div>
    <div class="contact contact--email">
      <span class="contact-label">email</span>
      <span class="contact-value">dlindqvist@kelmoraexample.com.pg</span>
    </div>
  </section>
</body>
</html>
```